Luxury packaging graphic design for a new Hair care elixir

We need a packaging design for a new product for our line extension of hair colouring. We have already a packaging that is very well received (all in pink) including all accesories and transport box (attached files).
For a new product - protein for the hair - we need a different design tapping into luxury segment.

Target Market(s)

This product is mainly for women between 25-65 that are looking forward to improve hair strukture and make hair looks better, nicer, softer, healthier. The product in the packaging could be used up to 2x times.

Industry/Entity Type

Hair And Beauty

Font styles to use
Serif
Sans Serif

Colors

Designer to choose colors to be used in the design.

Requirements
Must have
• The material of the packaging are carton/styropor/and glass (attached a picture of packaging design to be adapted). The components are quite small so the packaging plays a big role to increase the value of what it is inside. The packaging needs to be inline with our actual packaging designs and corporate identity as they may be delivered together so as an assamble it should look nice, beautiful and of high quality.
• The graphic design for the different components to be adapted are:
• - grapich design for outside box
• - graphic design for the inside bottles
• - graphic design for the flyer/instructions inside the box
Nice to have
• It needs to feel that the packaging is Wow! It is going to be delivered per post so there have to be a beautiful opening effect. Eventually to work with colours like black, white and gold would give a nice luxury feeling.
• The actual product inside is a concentrated protein component so it is very small, therefore the packaging should show that even if small it is an elixir for the hair.
Should not have
• a totally diffenet look as our actual designs.

```html
<!DOCTYPE html>
<html lang="en">
<head>
<meta charset="UTF-8">
<title>Nora Vel – Hair Elixier Packaging</title>
<link href="https://fonts.googleapis.com/css2?family=Jost:wght@400;500&display=swap" rel="stylesheet">
<style>
  :root {
    --paper: #ffffff;
    --panel: #0d0c0a;
    --gold: #c9a646;
    --gold-deep: #6e5620;
    --white: #ffffff;
    --caption: #222222;
  }
  html, body {
    margin: 0;
    padding: 0;
    width: 735px;
    height: 1200px;
    overflow: hidden;
    background: var(--paper);
  }
  .sheet {
    position: relative;
    width: 735px;
    height: 1200px;
  }
  .panel-caption {
    position: absolute;
    font-family: "Jost", sans-serif;
    font-size: 9px;
    letter-spacing: 1px;
    color: var(--caption);
    transform: rotate(-90deg);
    transform-origin: left top;
  }
  .panel {
    position: absolute;
    background: var(--panel);
    overflow: hidden;
  }
  .panel-pattern {
    position: absolute;
    inset: 0;
    background:
      radial-gradient(ellipse at 30% 30%, rgba(201,166,70,0.45), transparent 60%),
      radial-gradient(ellipse at 75% 70%, rgba(201,166,70,0.4), transparent 60%),
      linear-gradient(160deg, var(--gold-deep), var(--panel) 45%, var(--gold-deep) 75%, var(--panel));
  }
  .panel-frame {
    position: absolute;
    inset: 7px;
    border: 1px solid var(--gold);
  }
  .brand-mark {
    position: absolute;
    left: 0;
    right: 0;
    text-align: center;
    color: var(--white);
    font-family: "Jost", sans-serif;
  }
  .brand-name {
    display: block;
    font-weight: 500;
    text-transform: uppercase;
    line-height: 1;
  }
  .brand-tagline {
    display: block;
    font-weight: 400;
    text-transform: uppercase;
  }
  .product-name,
  .product-type,
  .product-volume {
    position: absolute;
    left: 0;
    right: 0;
    text-align: center;
    font-family: "Jost", sans-serif;
    color: var(--white);
    line-height: 1;
  }
  .product-name { font-weight: 500; }

  /* top panel */
  .box-top { left: 61px; top: 33px; width: 359px; height: 362px; }
  .box-top .brand-mark { top: 170px; }
  .box-top .brand-name { font-size: 44px; letter-spacing: 6px; }
  .box-top .brand-tagline { font-size: 14px; letter-spacing: 2px; margin-top: 12px; }

  /* front panel */
  .box-front { left: 61px; top: 418px; width: 359px; height: 751px; }
  .box-front .brand-mark { top: 107px; }
  .box-front .brand-name { font-size: 44px; letter-spacing: 6px; }
  .box-front .brand-tagline { font-size: 14px; letter-spacing: 2px; margin-top: 12px; }
  .box-front .product-name { top: 486px; font-size: 24px; letter-spacing: 3px; }
  .box-front .product-type { top: 536px; font-size: 12px; letter-spacing: 1px; }
  .box-front .product-volume { top: 681px; font-size: 11px; }

  /* bottle label */
  .bottle-label { left: 470px; top: 755px; width: 227px; height: 385px; }
  .bottle-label .panel-frame { inset: 5px; }
  .bottle-label .brand-mark { top: 42px; }
  .bottle-label .brand-name { font-size: 26px; letter-spacing: 4px; }
  .bottle-label .brand-tagline { font-size: 8px; letter-spacing: 1px; margin-top: 7px; }
  .bottle-label .product-name { top: 240px; font-size: 14px; letter-spacing: 2px; }
  .bottle-label .product-type { top: 264px; font-size: 7px; }
  .bottle-label .product-volume { top: 358px; font-size: 6px; }
</style>
</head>
<body>
<main class="sheet">

  <span class="panel-caption" style="left:30px; top:372px;">TOP</span>
  <section class="panel box-top">
    <div class="panel-pattern" role="img" aria-label="Flowing gold line pattern of wavy hair strands on black"></div>
    <div class="panel-frame"></div>
    <div class="brand-mark">
      <span class="brand-name">nora vel</span>
      <span class="brand-tagline">Shades of your own</span>
    </div>
  </section>

  <span class="panel-caption" style="left:30px; top:483px;">FRONT</span>
  <section class="panel box-front">
    <div class="panel-pattern" role="img" aria-label="Flowing gold line pattern of wavy hair strands on black"></div>
    <div class="panel-frame"></div>
    <div class="brand-mark">
      <span class="brand-name">nora vel</span>
      <span class="brand-tagline">Shades of your own</span>
    </div>
    <div class="product-name">HAIR ELIXIER</div>
    <div class="product-type">Concentrated Serum</div>
    <div class="product-volume">60ml e</div>
  </section>

  <section class="panel bottle-label">
    <div class="panel-pattern" role="img" aria-label="Flowing gold line pattern of wavy hair strands on black"></div>
    <div class="panel-frame"></div>
    <div class="brand-mark">
      <span class="brand-name">nora vel</span>
      <span class="brand-tagline">Shades of your own</span>
    </div>
    <div class="product-name">HAIR ELIXIER</div>
    <div class="product-type">Concentrated Serum</div>
    <div class="product-volume">60ml</div>
  </section>

</main>
</body>
</html>
```